Need Business Card Design, Letterhead and a Basic Form layout based on Existing Logo

We need (1) a business card design, (2) a letterhead design and (3) a basic form layout for an international holding company. This holding company has just formed two (2) sub-companies. The logo is the same for each company with only a simple word change for each company. The business card, letterhead and form design will be essentially the same for each company... with only the one word change being different.
The names of the companies are as follows:
1. Ridgeway Trust Services
2. Ridgeway Immigration Services
The design for the business card, letterhead and Form must be strong, clean and classy.
Our clients will be older, wealthy and mostly Asian. The design must project strength, stability and confidence.
The card may contain the following data:
1. The Logo
2. The name of the person
3. The title of the person
4. The address of the company
5. The Company Phone number
6. The personal mobile number
7. The Skype number (VOIP)
8. The WICKR number (IM)
9. The email
10. The website
We will attach AI files of our logo for the "Ridgeway Trust Services" company in the colors Black/White and Blue in both Horizontal and Vertical format... We have also included separate files of the logo icon.
We uploaded the AI files to give the designer the maximum options regarding color and effects. We included the separate files for the icon because we would like to give the designer the option of a watermark. Also, we think it might be nice to highlight the icon on the back of the card perhaps with the website address.
We are not sure which colors or color combinations would be best for these two companies. We know the colors must again project strength, stability and confidence. Perhaps, a combination that might include Tan, Black and White... not sure... need design help... remember this has to have the presence of a bank-like institution... no cartoonish designs or flashy color combinations... please.
The basic form layout will be used for various questionaires, input sheets and instructions.... etc.
NOTE: The fonts used in the logo are Trajan Pro Bold for word "RIDGEWAY" and Trajan Pro Regular for "XXXXXXXXX SERVICES".

```html
<!DOCTYPE html>
<html lang="en">
<head>
<meta charset="utf-8">
<title>Ridgeway Trust Services – Business Card</title>
<link href="https://fonts.googleapis.com/css2?family=Aldrich&display=swap" rel="stylesheet">
<style>
  :root {
    --backdrop: #e4e4e6;
    --card: #ffffff;
    --card-shade: #f1f1f3;
    --ink: #2b2b2d;
    --band: #262628;
    --band-light: #3c3c3f;
    --accent: #3a3a9e;
    --icon-ink: #ffffff;
  }
  * { box-sizing: border-box; margin: 0; padding: 0; }
  html, body {
    width: 1200px; height: 901px; overflow: hidden;
    background: var(--backdrop);
    font-family: "Aldrich", "Arial", sans-serif;
    color: var(--ink);
  }
  .sheet {
    position: relative; width: 1200px; height: 901px;
    display: flex; flex-direction: column; align-items: center; justify-content: center; gap: 36px;
  }
  .card {
    position: relative; width: 700px; height: 400px;
    background: linear-gradient(135deg, var(--card) 40%, var(--card-shade));
    border-bottom: 7px solid var(--accent);
    box-shadow: 0 6px 18px rgba(0,0,0,.18);
    overflow: hidden;
  }
  .card-bands { position: absolute; inset: 0; width: 100%; height: 100%; }
  .band { fill: var(--band); }
  .band-fold { fill: var(--band-light); }

  .brand { position: absolute; display: flex; align-items: center; gap: 16px; }
  .brand-mark { width: 46px; height: 46px; background: var(--ink); flex: none; }
  .brand-name {
    font-size: 30px; letter-spacing: 2px; color: var(--ink); line-height: 1.15;
  }
  .brand-name span { display: block; font-size: 15px; letter-spacing: 3px; }

  .card-back .brand { left: 0; right: 0; top: 130px; flex-direction: column; gap: 18px; text-align: center; }
  .card-back .brand-mark { width: 70px; height: 70px; transform: rotate(45deg); }
  .card-back .brand-name { font-size: 36px; }
  .card-back .brand-name span { font-size: 17px; }

  .card-front .brand { left: 250px; top: 110px; }

  .holder { position: absolute; left: 40px; top: 235px; }
  .holder-name { font-size: 19px; letter-spacing: 1px; color: var(--accent); text-transform: uppercase; }
  .holder-title { font-size: 11px; letter-spacing: 1px; text-transform: uppercase; margin-top: 3px; }

  .contact-list { list-style: none; display: flex; flex-direction: column; gap: 8px; }
  .contact-list li { display: flex; align-items: center; gap: 12px; font-size: 13px; letter-spacing: .5px; }
  .contact-icon {
    width: 24px; height: 24px; background: var(--accent); flex: none;
    display: flex; align-items: center; justify-content: center;
  }
  .contact-icon svg { width: 14px; height: 14px; fill: var(--icon-ink); stroke: var(--icon-ink); }
  .contact-personal { position: absolute; left: 40px; top: 288px; }
  .contact-web { position: absolute; left: 440px; top: 215px; }
</style>
</head>
<body>
<main class="sheet">

  <section class="card card-back" aria-label="Business card back">
    <svg class="card-bands" viewBox="0 0 700 400" aria-hidden="true">
      <polygon class="band" points="0,110 190,28 270,36 210,62 0,172"/>
      <polygon class="band-fold" points="190,28 270,36 230,20"/>
      <polygon class="band" points="520,0 590,0 700,82 700,150"/>
    </svg>
    <div class="brand">
      <div class="brand-mark" aria-hidden="true"></div>
      <div class="brand-name">RIDGEWAY<span>TRUST SERVICES</span></div>
    </div>
  </section>

  <section class="card card-front" aria-label="Business card front">
    <svg class="card-bands" viewBox="0 0 700 400" aria-hidden="true">
      <polygon class="band" points="405,40 470,36 700,84 700,132 455,82 480,62"/>
      <polygon class="band" points="230,0 290,0 0,240 0,180"/>
    </svg>

    <div class="brand">
      <div class="brand-mark" aria-hidden="true"></div>
      <div class="brand-name">RIDGEWAY<span>TRUST SERVICES</span></div>
    </div>

    <div class="holder">
      <p class="holder-name">Daniel Whitmore</p>
      <p class="holder-title">Financial Advisor</p>
    </div>

    <ul class="contact-list contact-personal">
      <li>
        <span class="contact-icon"><svg viewBox="0 0 14 14"><path d="M7 1a4 4 0 0 0-4 4c0 3 4 8 4 8s4-5 4-8a4 4 0 0 0-4-4zm0 5.5A1.5 1.5 0 1 1 7 3.5a1.5 1.5 0 0 1 0 3z" stroke="none"/></svg></span>
        Harbour Road, 18
      </li>
      <li>
        <span class="contact-icon"><svg viewBox="0 0 14 14"><path d="M3 1l2.5 0 1 3-1.5 1.2a7 7 0 0 0 3.8 3.8L10 7.5l3 1V11c0 1-1 2-2 2C6 13 1 8 1 3c0-1 1-2 2-2z" stroke="none"/></svg></span>
        020 555 0148
      </li>
      <li>
        <span class="contact-icon"><svg viewBox="0 0 14 14"><rect x="1" y="3" width="12" height="8" fill="none" stroke-width="1.4"/><path d="M1 3l6 5 6-5" fill="none" stroke-width="1.4"/></svg></span>
        dan@ridgewaymail.com
      </li>
    </ul>

    <ul class="contact-list contact-web">
      <li>
        <span class="contact-icon"><svg viewBox="0 0 14 14"><circle cx="7" cy="7" r="5.5" fill="none" stroke-width="1.2"/><ellipse cx="7" cy="7" rx="2.4" ry="5.5" fill="none" stroke-width="1.1"/><line x1="1.5" y1="7" x2="12.5" y2="7" stroke-width="1.1"/></svg></span>
        www.ridgewaytrust.com
      </li>
      <li>
        <span class="contact-icon"><svg viewBox="0 0 14 14"><rect x="4" y="4" width="6" height="6" stroke="none"/></svg></span>
        www.ridgewaynews.com
      </li>
      <li>
        <span class="contact-icon"><svg viewBox="0 0 14 14"><rect x="4" y="4" width="6" height="6" stroke="none"/></svg></span>
        www.ridgewayclub.com
      </li>
    </ul>
  </section>

</main>
</body>
</html>
```